Modern and Vibrant Car Wash Website

In Summary: A website using our Menus for Exterior and Full Service Car Washes: Marbleford, popular car wash, Quill and Pebble Lane Car Wash websites (link attached below are good references for the type of cartoony fun design).

I will add our flyer, and menus, and some other graphics as a visual reference. Will over time add the files (AI and SVG so you can use them).

Car wash front page should be nice and clean. I have lots of videos and photos we can use throughout the wash. Would like a video on the landing page.

Our shop section can remain blank as my POS developers will create a hyperlink to it.

Main easy to use functions should be the Car Wash services, their price and full service ones as well. Allow customers to see, book if needed etc.

Please note I have the website on DOMA.

I have attached a general pdf as well for some more info.

https://marblefordcarwash.example.ca/
https://trevinocarwash.example.ca/
https://glimmoncarwash.example.com/
https://quillwash.example.com/
https://vandrelpages.example.com/carwash-website-design/
https://pebblelanecarwash.example.com/

```html
<!DOCTYPE html>
<html lang="en">
<head>
<meta charset="utf-8">
<title>Gleam N' Go — Car Wash</title>
<link href="https://fonts.googleapis.com/css2?family=Orbitron:wght@400;500;600;700&family=Lato:wght@400;700&display=swap" rel="stylesheet">
<style>
:root{
  --page:#cfdce7;
  --blue:#1466bf;
  --blue-dark:#0d4f99;
  --blue-band:#0f62b3;
  --navy:#0b2d5c;
  --yellow:#e9b914;
  --yellow-line:#d4a80f;
  --ink:#111418;
  --muted:#3d4650;
  --chip:#7d9cbc;
  --footer:#c7d3de;
  --white:#ffffff;
}
*{box-sizing:border-box;margin:0;padding:0}
html,body{width:1200px;height:4067px;overflow:hidden}
body{position:relative;background:var(--page);font-family:'Lato',sans-serif;color:var(--ink)}
.abs{position:absolute}
.display{font-family:'Orbitron',sans-serif}
.media{position:absolute;overflow:hidden}
.media-photo{border-radius:18px;box-shadow:0 14px 30px rgba(11,45,92,.18)}
.pill-btn{position:absolute;display:flex;align-items:center;justify-content:space-between;padding:0 8px 0 14px;border-radius:30px;background:linear-gradient(90deg,#7fb0e8,#3f86d6);color:var(--white);font-size:14px;box-shadow:0 4px 10px rgba(20,102,191,.3)}
.pill-btn .arrow{width:28px;height:28px;border-radius:50%;background:var(--navy);display:flex;align-items:center;justify-content:center}
.section-title{position:absolute;font-family:'Orbitron',sans-serif;font-weight:500;font-size:32px;display:flex;align-items:center;gap:14px}
.wheel{width:28px;height:28px}
p.body{font-size:12px;line-height:16px;color:var(--muted)}
.pkg-row{position:absolute;left:150px;width:900px;border-bottom:1px solid var(--yellow-line);display:flex;align-items:center;justify-content:space-between;height:56px}
.pkg-row .name{font-family:'Orbitron',sans-serif;font-size:20px;color:#2a2a2a}
.plus{width:22px;height:22px;border-radius:50%;background:#b99a2b;color:#fff;display:flex;align-items:center;justify-content:center;font-size:16px;margin-right:10px}
.chip{height:30px;padding:0 14px;border-radius:20px;background:var(--blue);color:#fff;font-size:14px;display:flex;align-items:center;gap:6px}
.addon-btn{position:absolute;left:152px;width:248px;height:38px;background:var(--chip);color:#1d2733;display:flex;align-items:center;justify-content:center;font-size:16px;border-radius:2px}
.addon-btn.active{background:#e4ecf3;border:1.5px solid var(--chip);font-weight:700}
.social-dot{position:absolute;width:26px;height:26px;border-radius:50%;background:var(--blue)}
</style>
</head>
<body>

<!-- HERO -->
<section class="hero">
  <div class="media" role="img" aria-label="Background photo of a car being washed with foam and a rotating brush" style="left:0;top:0;width:1200px;height:780px;background:radial-gradient(ellipse at 80% 20%,#e98b8a 0%,rgba(233,139,138,0) 35%),radial-gradient(ellipse at 95% 50%,#f2c74a 0%,rgba(242,199,74,0) 30%),linear-gradient(180deg,#dbe8f2 0%,#c6dbec 60%,var(--page) 100%)"></div>

  <svg class="abs" style="left:150px;top:46px" width="32" height="24" viewBox="0 0 32 24"><rect y="1" width="32" height="3" fill="#111"/><rect y="10" width="24" height="3" fill="#111"/><rect y="19" width="32" height="3" fill="#111"/></svg>

  <div class="abs display" style="left:430px;top:46px;width:180px;text-align:center;font-size:20px;font-weight:700;color:var(--blue-dark)">Gleam N' Go</div>

  <div class="abs" style="left:845px;top:40px;width:150px;height:39px;border:1.5px solid #4b5560;border-radius:20px;display:flex;align-items:center;justify-content:space-between;padding:0 12px;font-size:14px;color:#4b5560">Search
    <svg width="16" height="16" viewBox="0 0 16 16"><circle cx="7" cy="7" r="5" fill="none" stroke="#4b5560" stroke-width="1.6"/><path d="M11 11l4 4" stroke="#4b5560" stroke-width="1.6"/></svg>
  </div>
  <div class="abs" style="left:1006px;top:37px;width:44px;height:44px;border-radius:50%;background:var(--blue);display:flex;align-items:center;justify-content:center">
    <svg width="18" height="20" viewBox="0 0 18 20"><circle cx="9" cy="6" r="4" fill="#fff"/><path d="M1 19c0-5 4-7 8-7s8 2 8 7z" fill="#fff"/></svg>
  </div>

  <div class="abs display" style="left:292px;top:208px;width:616px;text-align:center;font-size:13px;letter-spacing:14px;color:var(--ink)">Key Your Car Clean Always</div>
  <div class="abs display" style="left:200px;top:226px;width:800px;text-align:center;font-size:52px;font-weight:500;color:var(--ink)">Discover How We Are</div>
  <div class="abs display" style="left:200px;top:286px;width:800px;text-align:center;font-size:66px;font-weight:700;color:var(--blue-dark)">Changing</div>

  <div class="pill-btn" style="left:529px;top:384px;width:139px;height:40px">Book Now <span class="arrow"><svg width="12" height="12" viewBox="0 0 12 12"><path d="M2 2l8 8M10 3v7H3" stroke="#fff" stroke-width="1.6" fill="none"/></svg></span></div>

  <div class="abs" style="left:1030px;top:278px;width:18px;height:160px">
    <div style="width:16px;height:16px;border-radius:4px;background:var(--navy);margin-bottom:14px"></div>
    <div style="width:16px;height:16px;border-radius:4px;background:var(--navy);margin-bottom:14px"></div>
    <div style="width:16px;height:16px;border-radius:50%;background:var(--navy);margin-bottom:14px"></div>
    <div style="width:16px;height:16px;border-radius:4px;background:var(--navy);margin-bottom:8px"></div>
    <div style="width:2px;height:48px;background:var(--navy);margin-left:7px"></div>
  </div>

  <div class="media media-photo" role="img" aria-label="Orange sports car with a technician polishing its front wheel" style="left:466px;top:466px;width:671px;height:260px;background:linear-gradient(135deg,#f7b171 0%,#ee7a2c 40%,#c24c15 75%,#7a3217 100%)"></div>

  <div class="abs" style="left:152px;top:581px;width:285px;height:139px;background:var(--blue);border-radius:4px;padding:20px 14px;color:#fff">
    <div class="display" style="font-size:17px;font-weight:500">Professional Services</div>
    <div style="font-size:11.5px;line-height:15px;margin-top:10px;width:235px">There Are Many Variations Of Passages Of Lorem Ipsum Available, But The Majority Have Suffered Alteration In Some Form <span style="color:var(--yellow)">Read More.</span></div>
    <div style="position:absolute;right:8px;top:8px;width:28px;height:28px;border-radius:50%;background:#fff;border:3px solid #4a94e0"></div>
  </div>
</section>

<!-- WHY -->
<section class="why">
  <div class="media" role="img" aria-label="Car wash worker with a foam sprayer beside a soaped car" style="left:152px;top:790px;width:437px;height:292px;border:3px solid var(--blue);border-radius:6px;background:linear-gradient(135deg,#d7d9db,#7b8188 60%,#3c4148)"></div>

  <div class="section-title" style="left:647px;top:797px">Why Gleam N' Go
    <svg class="wheel" viewBox="0 0 28 28"><circle cx="14" cy="14" r="11" fill="none" stroke="#111" stroke-width="2.5"/><circle cx="14" cy="14" r="4" fill="#111"/></svg>
  </div>
  <p class="body abs" style="left:646px;top:845px;width:410px">Lorem Ipsum Dolor Sit Amet, Consectetur Adipiscing Elit, Sed Do Eiusmod Tempor Incididunt Ut Labore Et Dolore Magna Aliqua. Ut Enim Ad Minim Veniam, Quis Nostrud Exercitation Ullamco Laboris Nisi Ut Aliquip Ex Ea Commodo Consequat. Duis Aute Irure Dolor In Reprehenderit In Volupta Te Velit Esse Cillum.</p>
  <p class="body abs" style="left:646px;top:943px;width:410px">Dolore Eu Fugiat Nulla Pariatur. Excepteur Sint Occaecat Cupidatat Non Proident, Sunt In Culpa Qui Officia Deserunt Mollit Anim Id Est Laborum. Dolore Eu Fugiat Nulla Pariatur. Excepteur Sint Occaecat Cupidatat Non.</p>
  <div class="pill-btn" style="left:646px;top:1028px;width:139px;height:44px">Read More <span class="arrow"><svg width="12" height="12" viewBox="0 0 12 12"><path d="M2 2l8 8M10 3v7H3" stroke="#fff" stroke-width="1.6" fill="none"/></svg></span></div>
</section>

<!-- PACKAGES -->
<section class="packages">
  <div class="section-title" style="left:0;width:1200px;justify-content:center;top:1140px">Our Packages
    <svg class="wheel" viewBox="0 0 28 28"><circle cx="14" cy="14" r="11" fill="none" stroke="#111" stroke-width="2.5"/><circle cx="14" cy="14" r="4" fill="#111"/></svg>
  </div>
  <div class="abs" style="left:330px;top:1192px;width:540px;text-align:center;font-size:12px;line-height:16px">If You Are Going To Use A Passage Of Lorem Ipsum, You Need To Be Sure There Isn't Anything Embarrassing Hidden In The Middle Of Text.</div>
  <div class="abs display" style="left:520px;top:1236px;font-size:14px;font-weight:600;border-bottom:2px solid var(--ink);padding:0 6px 2px">Interior</div>
  <div class="abs display" style="left:620px;top:1236px;font-size:14px;font-weight:600">Exterior</div>

  <div class="abs" style="left:0;top:1285px;width:1200px;height:548px;background:var(--yellow)"></div>
  <div class="abs display" style="left:494px;top:1315px;font-size:14px;font-weight:600">Includes</div>
  <div class="abs display" style="left:870px;top:1315px;font-size:14px;font-weight:600">Price</div>
  <div class="abs" style="left:150px;top:1348px;width:900px;border-top:1px solid var(--yellow-line)"></div>

  <div class="pkg-row" style="top:1350px"><span class="name">Express Clean</span><span class="plus">+</span></div>

  <div class="abs" style="left:150px;top:1420px;width:900px;height:40px;display:flex;align-items:center">
    <span class="display" style="font-size:19px;font-weight:700;width:345px">Ultimate Ceramic Shine</span>
    <span style="font-size:9px;width:106px">Signature Shine</span>
    <span style="font-size:9px;width:94px">Ceramic Seal</span>
    <span style="font-size:9px">Premium Upgrades</span>
  </div>
  <svg class="abs" style="left:874px;top:1420px" width="88" height="42" viewBox="0 0 88 42"><path d="M10 4h64l12 17-12 17H10L2 21z" fill="var(--blue)" stroke="#6eaaf0" stroke-width="2"/><text x="20" y="27" fill="#fff" font-family="Lato" font-size="18">$25</text><text x="52" y="29" fill="#fff" font-family="Lato" font-size="8">99</text></svg>
  <div class="abs display" style="left:150px;top:1474px;font-size:14px;font-weight:600">Services</div>
  <div class="abs" style="left:150px;top:1503px;width:900px;height:68px;background:#c9a934;border:2px solid #8a8a4a;border-radius:6px;display:flex;align-items:center;justify-content:space-between;padding:0 14px">
    <span class="chip">✦ Under Spray</span><span class="chip">✦ Bumper Blaster</span><span class="chip">✦ Triple Soap</span><span class="chip">✦ Rim &amp; Wheel Cleaner</span><span class="chip">✦ Hot Wax N' Shine</span>
  </div>

  <div class="pkg-row" style="top:1575px;border-top:1px solid var(--yellow-line)"><span class="name">Signature Shine</span><span class="plus">+</span></div>
  <div class="pkg-row" style="top:1631px"><span class="name">Pro Shine</span><span class="plus">+</span></div>
  <div class="pkg-row" style="top:1687px"><span class="name">Complete Clean</span><span class="plus">+</span></div>
  <div class="pkg-row" style="top:1743px"><span class="name">Value Shine</span><span class="plus">+</span></div>
</section>

<!-- ADD-ON -->
<section class="addons">
  <div class="section-title" style="left:152px;top:1892px">Add - On
    <svg class="wheel" viewBox="0 0 28 28"><circle cx="14" cy="14" r="11" fill="none" stroke="#111" stroke-width="2.5"/><circle cx="14" cy="14" r="4" fill="#111"/></svg>
  </div>
  <div class="abs" style="left:152px;top:1946px;width:390px;font-size:11.5px;line-height:16px">If You Are Going To Use A Passage Of Lorem Ipsum, You Need To Be Sure There Isn't Anything Embarrassing Hidden In The Middle Of Text. All The Lorem Ipsum Generators On The Internet Tend To Repeat Predefined Chunks As Necessary <span style="color:var(--blue)">Read More.</span></div>

  <div class="addon-btn" style="top:2051px">Dash Dressing</div>
  <div class="addon-btn active" style="top:2103px">Seats Deep Shampoo</div>
  <div class="addon-btn" style="top:2155px">Pet Hair Lift</div>
  <div class="addon-btn" style="top:2207px">Mats &amp; Floor Shampoo</div>
  <div class="addon-btn" style="top:2260px">Mats Only-Shampoo</div>
  <div class="addon-btn" style="top:2312px">Leather Clean &amp; Condition</div>
  <div class="addon-btn" style="top:2364px">Trunk Vacuum</div>
  <div class="addon-btn" style="top:2416px">Wheel Spa</div>

  <div class="abs" style="left:437px;top:2116px;width:260px">
    <div style="font-size:17px;font-weight:700">Seats Deep Shampoo <span style="color:var(--blue)">✦</span></div>
    <div style="font-size:11.5px;line-height:16px;margin-top:8px">I Must Explain To You How All This Mistaken Idea Of Denouncing Pleasure And Praising Pain Was Born And I Will Give You A Complete Account Of The System, And Expound The Actual Teachings Of The Great <span style="color:var(--blue)">Read More.</span></div>
    <div style="font-size:9px;margin-top:8px">Our Price</div>
    <div style="font-size:21px;font-weight:700;margin-top:2px">From $59.99</div>
  </div>

  <div class="media" role="img" aria-label="Detailer vacuuming the front seat of a car interior" style="left:722px;top:1945px;width:325px;height:509px;border:3px solid var(--blue);border-radius:44px;background:linear-gradient(160deg,#d9dcdf 0%,#8a8f96 45%,#2b2f35 100%)"></div>
</section>

<!-- CHAMPION -->
<section class="champion">
  <div class="section-title" style="left:0;width:1200px;justify-content:center;top:2564px">The Champion Treatment
    <svg class="wheel" viewBox="0 0 28 28"><circle cx="14" cy="14" r="11" fill="none" stroke="#111" stroke-width="2.5"/><circle cx="14" cy="14" r="4" fill="#111"/></svg>
  </div>
  <div class="abs" style="left:160px;top:2620px;width:880px;text-align:center;font-size:11.5px;line-height:16px">At Vero Eos Et Accusamus Et Iusto Odio Dignissimos Ducimus Qui Blanditiis Praesentium Voluptatum Deleniti Atque Corrupti Quos Dolores Et Quas Molestias Excepturi Sint Occaecati Cupiditate Non Provident, Similique Sunt In Culpa Qui Officia Deserunt Mollitia Animi, Id Est Laborum Et Dolorum Fuga.</div>
  <div class="media media-photo" role="img" aria-label="Silver sedan shown half muddy and half freshly cleaned, split by a comparison slider" style="left:202px;top:2692px;width:793px;height:261px;background:linear-gradient(90deg,#8d7a62 0%,#b3a893 30%,#cfcbc3 49.6%,#e9ecf0 50.4%,#f5f6f8 80%,#dfe3e8 100%)"></div>
  <div class="abs" style="left:597px;top:2692px;width:3px;height:261px;background:#fff"></div>
  <div class="abs" style="left:587px;top:2812px;width:23px;height:23px;border-radius:50%;background:#fff;border:2px solid #c9ced5"></div>
</section>

<!-- FAQ BAND -->
<section class="faq">
  <div class="abs" style="left:0;top:3005px;width:1200px;height:335px;background:linear-gradient(90deg,var(--blue-band) 0%,#1c6ec0 70%,#6d8fb0 100%)"></div>
  <div class="abs display" style="left:0;top:3058px;width:1200px;text-align:center;font-size:30px;color:#dbe9f8">Got Any Questions On Our Car Cleaning Services ?</div>
  <div class="abs" style="left:0;top:3110px;width:1200px;text-align:center;font-size:11px;color:#3f7fc7">There's A 99.9% Chance The Answer To Your Question Has Been Answered Already.</div>
  <div class="pill-btn" style="left:537px;top:3155px;width:136px;height:43px">Our FAQ'S <span class="arrow"><svg width="12" height="12" viewBox="0 0 12 12"><path d="M2 2l8 8M10 3v7H3" stroke="#fff" stroke-width="1.6" fill="none"/></svg></span></div>
  <div class="abs display" style="left:140px;top:3262px;font-size:76px;font-weight:500;color:rgba(255,255,255,.22);white-space:nowrap">Gleam N'Go</div>
  <div class="media media-photo" role="img" aria-label="Mechanic in blue overalls leaning on a blue SUV" style="left:700px;top:3160px;width:390px;height:267px;background:linear-gradient(135deg,#5c87cf 0%,#2f5cb0 45%,#1d3f88 100%)"></div>
</section>

<!-- RESALE -->
<section class="resale">
  <div class="media media-photo" role="img" aria-label="Turquoise SUV front view in a soft cloud of foam" style="left:221px;top:3458px;width:347px;height:253px;background:linear-gradient(160deg,#eef4f8 0%,#7fe3ea 30%,#2cc2d0 60%,#1a8f9c 100%)"></div>
  <div class="section-title" style="left:638px;top:3496px;line-height:38px;align-items:flex-start">Maintain Your Car's<br>Resale Value
    <svg class="wheel" viewBox="0 0 28 28" style="margin-top:6px"><circle cx="14" cy="14" r="11" fill="none" stroke="#111" stroke-width="2.5"/><circle cx="14" cy="14" r="4" fill="#111"/></svg>
  </div>
  <div class="abs" style="left:638px;top:3578px;width:420px;font-size:12px;line-height:16px">Stop Dirt, Debris, Dust And Rust From Depreciating The Value Of Your Car.</div>
  <div class="abs" style="left:638px;top:3608px;width:420px;font-size:12px;line-height:16px">There's A Cleaning Regimen That Will Work Wonders For Your Car And We Know Everything About It.</div>
  <div class="pill-btn" style="left:636px;top:3670px;width:135px;height:41px">Our Story <span class="arrow"><svg width="12" height="12" viewBox="0 0 12 12"><path d="M2 2l8 8M10 3v7H3" stroke="#fff" stroke-width="1.6" fill="none"/></svg></span></div>
</section>

<!-- FOOTER -->
<footer class="site-footer">
  <div class="abs" style="left:0;top:3758px;width:1200px;height:309px;background:var(--footer)"></div>
  <div class="abs display" style="left:440px;top:3816px;width:300px;text-align:center;font-size:26px;font-weight:700;color:var(--blue-dark)">Gleam N' Go</div>
  <div class="abs display" style="left:340px;top:3900px;width:500px;text-align:center;font-size:19px">Clean, Shine And Protect Your Car</div>

  <svg class="abs" style="left:150px;top:3866px" width="16" height="20" viewBox="0 0 16 20"><path d="M8 19s6-7 6-11A6 6 0 0 0 2 8c0 4 6 11 6 11z" fill="#111"/><circle cx="8" cy="8" r="2.2" fill="var(--footer)"/></svg>
  <div class="abs" style="left:177px;top:3862px;font-size:11px;line-height:15px">27 Harbour Row, Elmsdale ON<br>K0A 2B3.</div>
  <svg class="abs" style="left:150px;top:3906px" width="16" height="16" viewBox="0 0 16 16"><path d="M3 1l3 0 1 4-2 1c1 2 3 4 5 5l1-2 4 1v3c0 1-1 2-2 2C7 15 1 9 1 3c0-1 1-2 2-2z" fill="none" stroke="#111" stroke-width="1.3"/></svg>
  <div class="abs" style="left:177px;top:3907px;font-size:11px">(555) 014-WASH</div>

  <div class="abs" style="left:872px;top:3842px;width:176px;height:38px;border-radius:20px;background:linear-gradient(90deg,var(--navy),var(--blue));display:flex;align-items:center;justify-content:space-between;padding:0 6px 0 14px;color:#fff;font-size:12px">Your Email
    <span style="width:28px;height:28px;border-radius:50%;background:#6aa8ea;display:flex;align-items:center;justify-content:center"><svg width="12" height="12" viewBox="0 0 12 12"><path d="M1 6l10-5-3 10-2-4z" fill="#fff"/></svg></span>
  </div>
  <div class="social-dot" style="left:874px;top:3895px"></div>
  <div class="social-dot" style="left:912px;top:3895px"></div>
  <div class="social-dot" style="left:949px;top:3895px"></div>
  <div class="social-dot" style="left:987px;top:3895px"></div>

  <nav class="abs" style="left:371px;top:3954px;width:456px;height:43px;border:1.5px solid #3a4550;border-radius:22px;display:flex;align-items:center;justify-content:space-around;font-size:14px">
    <span>Home</span><span>About Us</span><span>Service</span><span>Package</span><span>Contact Us</span>
  </nav>
  <div class="abs" style="left:0;top:4049px;width:1200px;text-align:center;font-size:8px;color:#333">© 2025 The Gleam N' Go All Rights Reserved.</div>
</footer>

</body>
</html>
```